pharmacy/travel clinic business card design

We need a business card for our new business called Brenwick Travel Clinic and Pharmacy. Our primary focus is doing consultations for people before travelling internationally and providing vaccinations and prescriptions for them. While the business is considered a pharmacy, it has more the look and feel of a doctor's office. The design should communicate a professional and trustworthy feel. I have attached a copy of the logo we are going to be using.
Updates
Thanks for the submissions.  If you haven`t been eliminated you are one of the finalists.  Decision will likely be made tomorrow.

Target Market(s)
Customers, other health care professionals, travel agents
Industry/Entity Type
Clinic
Look and feel
Each slider illustrates characteristics of the customer's brand and the style your logo design should communicate.

```html
<!DOCTYPE html>
<html lang="en">
<head>
<meta charset="utf-8">
<title>Brenwick Travel Clinic and Pharmacy — Business Card</title>
<link rel="stylesheet" href="https://fonts.googleapis.com/css2?family=Arimo:wght@400;700&display=swap">
<style>
  :root {
    --card-bg: #ffffff;
    --brand-blue: #2a9ad6;
    --deep-blue: #1a5fa8;
    --ocean-blue: #0b8fd0;
    --sea-green: #2f9a6a;
    --sage-green: #8fbf8f;
    --pale-sage: #e3efe3;
    --text-blue: #2f9bd8;
  }
  html, body {
    margin: 0;
    padding: 0;
    width: 1200px;
    height: 800px;
    overflow: hidden;
    background: var(--card-bg);
  }
  .business-card {
    position: relative;
    width: 1200px;
    height: 800px;
    background: var(--card-bg);
    font-family: "Arimo", Arial, sans-serif;
    overflow: hidden;
  }
  .decor {
    position: absolute;
    inset: 0;
    width: 1200px;
    height: 800px;
  }
  .brand-name {
    position: absolute;
    left: 500px;
    top: 318px;
    display: flex;
    align-items: flex-start;
    gap: 18px;
    color: var(--brand-blue);
    font-weight: 700;
  }
  .brand-dot {
    width: 34px;
    height: 34px;
    margin-top: 14px;
    border-radius: 50%;
    background: var(--brand-blue);
    flex: none;
  }
  .brand-lines {
    display: flex;
    flex-direction: column;
    line-height: 1;
  }
  .brand-primary {
    font-size: 58px;
    letter-spacing: -1px;
  }
  .brand-secondary {
    font-size: 58px;
    letter-spacing: -1px;
    margin-top: 4px;
  }
  .brand-tertiary {
    font-size: 26px;
    margin-top: 10px;
    letter-spacing: 0.5px;
  }
  .contact-details {
    position: absolute;
    right: 34px;
    top: 610px;
    margin: 0;
    text-align: right;
    color: var(--text-blue);
    font-size: 37px;
    line-height: 42px;
    font-style: normal;
  }
  .contact-details p {
    margin: 0;
  }
</style>
</head>
<body>
  <main class="business-card">
    <svg class="decor" viewBox="0 0 1200 800" aria-hidden="false">
      <defs>
        <linearGradient id="wash-green" x1="0" y1="0" x2="1" y2="1">
          <stop offset="0" stop-color="var(--pale-sage)"/>
          <stop offset="0.55" stop-color="var(--sage-green)"/>
          <stop offset="1" stop-color="var(--sea-green)"/>
        </linearGradient>
        <linearGradient id="band-blue" x1="0" y1="0" x2="1" y2="1">
          <stop offset="0" stop-color="var(--deep-blue)"/>
          <stop offset="0.5" stop-color="var(--ocean-blue)"/>
          <stop offset="1" stop-color="var(--sea-green)"/>
        </linearGradient>
      </defs>
      <path role="img" aria-label="Decorative motif area in soft green tones"
            d="M0 0 H420 C470 160 430 330 360 430 C300 520 280 650 330 800 H0 Z"
            fill="url(#wash-green)" opacity="0.55"/>
      <path class="corner-band"
            d="M0 440 C110 440 250 460 310 480 C290 580 300 700 330 800 H0 Z"
            fill="url(#band-blue)"/>
    </svg>

    <div class="brand-name">
      <span class="brand-dot"></span>
      <div class="brand-lines">
        <span class="brand-primary">Brenwick</span>
        <span class="brand-secondary">Travel Clinic</span>
        <span class="brand-tertiary">and Pharmacy</span>
      </div>
    </div>

    <address class="contact-details">
      <p class="contact-tel">Tel: 000-000-0000</p>
      <p class="contact-fax">Fax: 000-000-0000</p>
      <p class="contact-email">Email: contactus@mycompany.com</p>
      <p class="contact-address">Address: Bienvenue a note company</p>
    </address>
  </main>
</body>
</html>
```